Standard Biz Card
Health Professionals
Please upload ai or eps of your logo
Kindly upload logo file in ai/eps format!
That contest is here: http://orders.markcraftplaza.example/contests/new-health-clinic-logo-biz-card
Sorry, there seem to be a misunderstandig as we thought this job was combined with the logo job. We do not have a logo yet, it is another contest going on at the moment.
Please upload the logo files

```html
<!DOCTYPE html>
<html lang="no">
<head>
<meta charset="utf-8">
<title>Lars Nilsen – Business Cards</title>
<link href="https://fonts.googleapis.com/css2?family=Arimo:wght@400;700&display=swap" rel="stylesheet">
<style>
  :root {
    --stage: #1d3342;
    --paper: #ffffff;
    --cyan: #1aa3d4;
    --orange: #ee9518;
    --lime: #a6d23c;
    --steel-blue: #5b8ccc;
    --ink: #333333;
    --white: #ffffff;
  }
  * { box-sizing: border-box; margin: 0; padding: 0; }
  html, body { width: 1200px; height: 655px; overflow: hidden; }
  body {
    background: var(--stage);
    font-family: "Arimo", Arial, sans-serif;
    position: relative;
  }
  .card {
    position: absolute;
    top: 137px;
    width: 506px;
    height: 290px;
    background: var(--paper);
    overflow: hidden;
  }
  .card--front { left: 89px; }
  .card--back { left: 622px; }

  .identity { position: absolute; }
  .card--front .identity { left: 0; right: 0; top: 218px; text-align: center; }
  .card--front .identity { top: 81px; }
  .card--back .identity { right: 17px; top: 12px; text-align: right; }

  .name { font-size: 19px; font-weight: 400; line-height: 1.2; }
  .role { font-size: 12px; line-height: 1.4; }
  .card--front .name { color: var(--orange); }
  .card--front .role { color: var(--ink); }
  .card--back .name { color: var(--lime); }
  .card--back .role { color: var(--steel-blue); }

  .accent-line { position: absolute; left: 0; right: 0; top: 209px; }
  .card--front .accent-line { height: 14px; background: var(--cyan); }
  .card--back .accent-line { height: 9px; background: var(--lime); }

  .contact-band {
    position: absolute; left: 0; right: 0; top: 223px; bottom: 0;
    color: var(--white);
    font-weight: 700;
    font-size: 13.5px;
    line-height: 19px;
    text-align: center;
    padding-top: 8px;
  }
  .card--front .contact-band { background: var(--orange); }
  .card--back .contact-band { background: var(--steel-blue); }

  .dots { position: absolute; left: 10px; top: 158px; }
</style>
</head>
<body>
  <section class="card card--front">
    <div class="identity">
      <p class="name">Lars Nilsen</p>
      <p class="role">Manuellterapeut</p>
    </div>
    <div class="accent-line"></div>
    <div class="contact-band">
      <p>Solbergveien 4| 1470 Lindvik</p>
      <p>social.example/vitalmt</p>
      <p>updates.example/vitalmt</p>
    </div>
  </section>

  <section class="card card--back">
    <div class="identity">
      <p class="name">Lars Nilsen</p>
      <p class="role">Manuellterapeut</p>
    </div>
    <svg class="dots" width="110" height="50" viewBox="0 0 110 50" aria-hidden="true">
      <circle cx="21" cy="22" r="19" fill="var(--lime)"/>
      <circle cx="64" cy="27" r="12" fill="var(--lime)"/>
      <circle cx="98" cy="31" r="7" fill="var(--lime)"/>
    </svg>
    <div class="accent-line"></div>
    <div class="contact-band">
      <p>Solbergveien 4| 1470 Lindvik</p>
      <p>social.example/vitalmt</p>
      <p>updates.example/vitalmt</p>
    </div>
  </section>
</body>
</html>
```